Makeupbyfernandflick banner

Hi I am a makeup artist looking at getting my banner created, I will be sending a picture below as a example of what I want, it's what an other makeup artist has done on her banner and I love it !
I will be also sending the pictures that you will need to put it together and will also attach a picture of what I would want written in the middle, please try and match the writing showen in the example.
Please feel free to ask any questions
Thank you
Marlene Tobrecht

```html
<!DOCTYPE html>
<html lang="en">
<head>
<meta charset="utf-8">
<title>Marlene Tobrecht – Makeup Artist Banner</title>
<link rel="stylesheet" href="https://fonts.googleapis.com/css2?family=Niconne&family=Didact+Gothic&display=swap">
<style>
  :root {
    --paper: #ffffff;
    --ink: #1c1c1c;
    --accent: #c8286e;
    --lip-light: #e2458d;
    --lip-deep: #a3114c;
    --brush-dark: #1e1e1e;
    --brush-grey: #9a9a9a;
    --powder: #e0467f;
  }
  html, body {
    margin: 0;
    padding: 0;
    overflow: hidden;
    background: var(--paper);
  }
  .banner {
    position: relative;
    width: 1200px;
    height: 2743px;
    background: var(--paper);
    overflow: hidden;
    font-family: "Didact Gothic", "Century Gothic", sans-serif;
    color: var(--ink);
  }
  .lips-art {
    position: absolute;
    left: 300px;
    top: 60px;
    width: 860px;
    height: 560px;
    border-radius: 50% 50% 46% 54% / 55% 55% 45% 45%;
    background: radial-gradient(ellipse at 40% 35%, var(--lip-light), var(--lip-deep) 78%);
    transform: rotate(25deg);
  }
  .artist-name {
    position: absolute;
    margin: 0;
    font-family: "Niconne", cursive;
    font-weight: 400;
    font-size: 215px;
    line-height: 1;
    color: var(--ink);
    white-space: nowrap;
  }
  .artist-name--first { left: 62px; top: 620px; }
  .artist-name--last { left: 312px; top: 822px; }
  .artist-role {
    position: absolute;
    right: 112px;
    top: 1068px;
    margin: 0;
    font-size: 78px;
    line-height: 1;
    color: var(--accent);
    white-space: nowrap;
  }
  .intro {
    position: absolute;
    left: 0;
    top: 1282px;
    width: 1200px;
    margin: 0;
    text-align: center;
    font-size: 76px;
    line-height: 88px;
    letter-spacing: 4px;
    color: var(--ink);
  }
  .social {
    position: absolute;
    top: 1968px;
    height: 108px;
    display: flex;
    align-items: center;
    gap: 24px;
    white-space: nowrap;
  }
  .social--feed { left: 144px; }
  .social--loop { left: 636px; }
  .social__dot {
    width: 96px;
    height: 96px;
    border-radius: 50%;
    background: var(--accent);
    flex: none;
  }
  .social__name {
    font-size: 60px;
    line-height: 1;
    color: var(--ink);
  }
  .brushes-photo {
    position: absolute;
    left: 120px;
    top: 2150px;
    width: 1010px;
    height: 510px;
    border-radius: 40% 12% 30% 40% / 50% 30% 50% 50%;
    background:
      radial-gradient(ellipse 30% 38% at 28% 68%, var(--powder), transparent 75%),
      linear-gradient(165deg, var(--brush-grey) 0%, var(--brush-dark) 55%, #eeeeee 100%);
  }
</style>
</head>
<body>
  <main class="banner">
    <div class="lips-art" role="img" aria-label="Illustration of glossy pink lips with teeth biting the lower lip"></div>

    <h1 class="artist-name artist-name--first">Marlene</h1>
    <p class="artist-name artist-name--last">Tobrecht</p>
    <p class="artist-role">| Makeup Artist |</p>

    <p class="intro">
      I will ad this text later.<br>
      Only an example for now.<br>
      I will ad this text later.<br>
      Only an example for now.<br>
      I will ad this text later.<br>
      Only an example for now.
    </p>

    <div class="social social--feed">
      <span class="social__dot"></span>
      <span class="social__name">Glowfeed</span>
    </div>
    <div class="social social--loop">
      <span class="social__dot"></span>
      <span class="social__name">Shimmerloop</span>
    </div>

    <div class="brushes-photo" role="img" aria-label="Photograph of black makeup brushes with pink blush powder scattered below"></div>
  </main>
</body>
</html>
```